Harbin Vale Co Tank Lining Services

I would check out our website for an a quick understanding of what Blasting and Painting "is". www.harbinvaleco.example

I need to Design "sales postcard" or "company postcard" that outlines the TANK LINING division of our company. (What is a "tank lining"? It is a coating applied to the interior of a Water Tank or "Water Tower". There are certifications and special equipment needed to provide these services that make it a unique market) This is a NEW service we are offing to our customers.

We want to include photo's of: Sand Blasting, Painting, and Welding on a Ground Storage Tank. (please see attached)

Bullet points to include:
-Critical Areas
-Tank Inspections
-Manway Installation
-Fire/Domestic Water

Please Note: a little says a lot in regards to regards to data crammed into "postcards". Our market is one that won't need to be "spoon" fed. I need potential clients to read the name and our contact info (obviously).

Target Market(s)

Building Owners

Industry/Entity Type

Construction

Font styles to use
Sans Serif

Colors
0054AA
0677BA
7BADD7
CADEEF
E8F1F8

Requirements
Must have
• Layered photos or pictures
Nice to have
• Cropped Layered photos are good
Should not have
• to much clutter

```html
<!DOCTYPE html>
<html lang="en">
<head>
<meta charset="utf-8">
<title>Harbin Vale Co — Tank Lining</title>
<link rel="stylesheet" href="https://fonts.googleapis.com/css2?family=Montserrat:wght@300;500;600;700;800&display=swap">
<style>
  :root {
    --navy: #121a4a;
    --yellow: #f6d04d;
    --gold: #ecbf2a;
    --field: #2f4aa0;
    --field-deep: #243f98;
    --bar: #0e56a8;
    --bullet: #0e6fc0;
    --white: #ffffff;
  }
  * { margin: 0; padding: 0; box-sizing: border-box; }
  html, body { width: 1200px; height: 655px; overflow: hidden; background: var(--field); }
  .postcard {
    position: relative; width: 1200px; height: 655px; overflow: hidden;
    font-family: "Montserrat", sans-serif; color: var(--navy);
  }
  .backdrop { position: absolute; inset: 0; }
  .brand {
    position: absolute; left: 55px; top: 52px;
    display: flex; align-items: center; gap: 10px;
    font-size: 23px; font-weight: 700; color: var(--navy);
  }
  .brand-mark { width: 30px; height: 30px; background: var(--navy); }
  .headline { position: absolute; left: 54px; top: 124px; font-weight: 800; line-height: 1; }
  .headline-top { display: block; font-size: 65px; letter-spacing: 1px; }
  .headline-main { display: block; font-size: 86px; margin-top: 2px; letter-spacing: 1px; }
  .services { position: absolute; left: 55px; top: 311px; list-style: none; }
  .services li {
    display: flex; align-items: center; height: 45.5px;
    font-size: 21px; font-weight: 600; letter-spacing: 1.2px;
  }
  .services li::before {
    content: ""; width: 0; height: 0; margin-right: 15px;
    border-left: 12px solid var(--bullet);
    border-top: 7px solid transparent; border-bottom: 7px solid transparent;
  }
  .call-bar {
    position: absolute; left: 0; top: 522px; width: 506px; height: 67px;
    background: var(--bar); border-radius: 0 34px 34px 0;
    display: flex; align-items: center; padding-left: 47px; gap: 24px;
    color: var(--white);
  }
  .call-bar svg { width: 46px; height: 46px; }
  .call-label { font-size: 29px; font-weight: 300; letter-spacing: 3px; }
  .call-number { font-size: 29px; font-weight: 700; letter-spacing: 2px; margin-left: 8px; }
  .work-label {
    position: absolute; top: 585px; width: 137px; height: 27px;
    background: var(--yellow); color: var(--navy);
    font-size: 15px; font-weight: 600; text-align: center; line-height: 27px;
  }
</style>
</head>
<body>
<div class="postcard">
  <svg class="backdrop" viewBox="0 0 1200 655" width="1200" height="655">
    <defs>
      <radialGradient id="tankGrad" cx="0.5" cy="0.45" r="0.6">
        <stop offset="0" stop-color="#cfc6b4"/><stop offset="1" stop-color="#8a8171"/>
      </radialGradient>
      <linearGradient id="blastGrad" x1="0" y1="0" x2="1" y2="1">
        <stop offset="0" stop-color="#d9d9dc"/><stop offset="1" stop-color="#4a4443"/>
      </linearGradient>
      <radialGradient id="paintGrad" cx="0.35" cy="0.3" r="0.8">
        <stop offset="0" stop-color="#f1f1ee"/><stop offset="1" stop-color="#8d8f8c"/>
      </radialGradient>
      <linearGradient id="weldGrad" x1="0" y1="0" x2="1" y2="1">
        <stop offset="0" stop-color="#e84a4e"/><stop offset="1" stop-color="#c21f2b"/>
      </linearGradient>
    </defs>
    <rect width="1200" height="655" fill="var(--field)"/>
    <rect y="613" width="1200" height="42" fill="var(--field-deep)"/>
    <polygon points="470,0 540,0 485,60" fill="var(--navy)" opacity="0.7"/>
    <path d="M84 0 H470 C520 160 560 330 582 445 C600 520 560 570 480 600 L363 655 H0 V80 Z" fill="var(--yellow)"/>
    <line x1="629" y1="65" x2="680" y2="-5" stroke="var(--gold)" stroke-width="22" stroke-linecap="round"/>
    <line x1="1200" y1="225" x2="1185" y2="250" stroke="var(--gold)" stroke-width="22" stroke-linecap="round"/>
    <g fill="var(--navy)"><circle cx="445" cy="33" r="3"/><circle cx="469" cy="33" r="3"/></g>
    <g fill="var(--navy)"><circle cx="501" cy="377" r="3"/><circle cx="501" cy="400" r="3"/><circle cx="501" cy="423" r="3"/></g>
    <g fill="var(--white)">
      <circle cx="628" cy="238" r="2"/><circle cx="643" cy="238" r="2"/><circle cx="658" cy="238" r="2"/>
      <circle cx="628" cy="252" r="2"/><circle cx="643" cy="252" r="2"/><circle cx="658" cy="252" r="2"/>
      <circle cx="628" cy="266" r="2"/><circle cx="643" cy="266" r="2"/><circle cx="658" cy="266" r="2"/>
    </g>
    <g fill="var(--gold)">
      <circle cx="1140" cy="18" r="3"/><circle cx="1152" cy="18" r="3"/><circle cx="1164" cy="18" r="3"/><circle cx="1176" cy="18" r="3"/><circle cx="1186" cy="18" r="3"/>
      <circle cx="1150" cy="29" r="3"/><circle cx="1162" cy="29" r="3"/><circle cx="1174" cy="29" r="3"/><circle cx="1186" cy="29" r="3"/>
      <circle cx="1162" cy="40" r="3"/><circle cx="1174" cy="40" r="3"/><circle cx="1186" cy="40" r="3"/>
      <circle cx="1174" cy="51" r="3"/><circle cx="1186" cy="51" r="3"/><circle cx="1186" cy="63" r="3"/>
    </g>
    <g fill="var(--white)"><circle cx="1170" cy="645" r="3"/><circle cx="1192" cy="645" r="3"/></g>

    <circle cx="900" cy="211" r="169" fill="none" stroke="var(--gold)" stroke-width="3" stroke-dasharray="12 9"/>
    <circle cx="900" cy="211" r="161" fill="url(#tankGrad)" role="img" aria-label="Photo of a ground storage tank interior with piping and a freshly lined floor"/>

    <circle cx="711" cy="494" r="76" fill="none" stroke="var(--gold)" stroke-width="2" stroke-dasharray="8 6"/>
    <circle cx="711" cy="494" r="70" fill="url(#blastGrad)" role="img" aria-label="Photo of a worker holding sand blasting hoses"/>
    <circle cx="902" cy="494" r="76" fill="none" stroke="var(--gold)" stroke-width="2" stroke-dasharray="8 6"/>
    <circle cx="902" cy="494" r="70" fill="url(#paintGrad)" role="img" aria-label="Photo of a freshly painted tank interior lit by a work lamp"/>
    <circle cx="1092" cy="494" r="76" fill="none" stroke="var(--gold)" stroke-width="2" stroke-dasharray="8 6"/>
    <circle cx="1092" cy="494" r="70" fill="url(#weldGrad)" role="img" aria-label="Photo of a welder working on a red tank wall with sparks"/>
  </svg>

  <div class="brand"><span class="brand-mark"></span>Harbin Vale Co</div>

  <h1 class="headline">
    <span class="headline-top">TANK</span>
    <span class="headline-main">LINING</span>
  </h1>

  <ul class="services">
    <li>Critical Areas</li>
    <li>Tank Inspections</li>
    <li>Manway Installation</li>
    <li>Fire/Domestic Water</li>
  </ul>

  <div class="call-bar">
    <svg viewBox="0 0 48 48" fill="none" stroke="#fff" stroke-width="2.6" stroke-linecap="round" stroke-linejoin="round">
      <path d="M10 6 l7 -1 l4 10 l-5 4 c2 6 6 10 12 12 l4 -5 l10 4 l-1 7 c-1 4 -5 6 -9 5 C18 38 8 28 5 14 c-1 -4 1 -7 5 -8z"/>
      <path d="M29 8 a12 12 0 0 1 11 11"/>
      <path d="M28 2 a18 18 0 0 1 18 18"/>
    </svg>
    <span><span class="call-label">Call Us:</span><span class="call-number">555-014-2738</span></span>
  </div>

  <div class="work-label" style="left:643px">Sand Blasting</div>
  <div class="work-label" style="left:834px">Painting</div>
  <div class="work-label" style="left:1024px">Welding</div>
</div>
</body>
</html>
```